Quillon Maison Wood Fired Pizza business card design

I have a logo and need an eye catching design that will get me noticed.
My business is wood fired pizza. I want a bold design that will make our customers remember us and the food that we serve. Work with the colors of our logo and texts. Maybe add designs that lend to what or how pizza is made using our wood fired oven?

Target Market(s)

Foodies!

Contact Information for Business Card

Quillon Maison Wood Fired Pizza
Our slogan is Fast. Fresh. Handcrafted
Catering for all events

Requirements
Must have
• Dana Porrick
Telephone 570 555 0183
website www.getquillon.example
Facebook @getquillonpizza maybe use the facebook logo next to it
Instagram getquillonpizza maybe use the instagram logo next to it
Catering for all events
Nice to have
• Maybe pizza peels, pizza cutters? Wood? Fired wood? Using our flame in the background?
Please work with different colored text so each sentence stands out? A themed color for facebook?
Maybe work with the colors within our logo?
Please try to use the our quillon font, but not a must have.

```html
<!DOCTYPE html>
<html lang="en">
<head>
<meta charset="utf-8">
<title>Quillon Maison Wood Fired Pizza – Business Card</title>
<link href="https://fonts.googleapis.com/css2?family=Roboto:wght@400;700&family=Courgette&family=Crimson+Pro:wght@600&display=swap" rel="stylesheet">
<style>
  :root {
    --backdrop: #e9e4dc;
    --card-black: #000000;
    --ember-orange: #f39a1f;
    --flame-red: #d32a2a;
    --text-white: #ffffff;
    --fire-deep: #7a1e05;
    --fire-mid: #e0520d;
    --fire-bright: #ffc24a;
    --crust: #c98a4a;
    --cheese: #efd9a8;
  }
  * { margin: 0; padding: 0; box-sizing: border-box; }
  html, body { width: 900px; height: 1200px; overflow: hidden; }
  body { background: var(--backdrop); position: relative; font-family: "Roboto", sans-serif; }

  .card {
    position: absolute; left: 82px; width: 733px; height: 429px;
    border-radius: 22px; overflow: hidden; background: var(--card-black);
    box-shadow: 0 6px 18px rgba(0,0,0,.25);
  }
  .card--front { top: 138px; }
  .card--back { top: 632px; }

  /* Front */
  .front-photo { position: absolute; right: 0; top: 0; width: 400px; height: 429px; }
  .brand-name {
    position: absolute; color: var(--text-white); font-family: "Roboto", sans-serif;
    font-weight: 700; white-space: nowrap; line-height: 1;
  }
  .card--front .brand-name { left: 44px; top: 72px; font-size: 32px; letter-spacing: 2.5px; }
  .holder-name {
    position: absolute; left: 46px; top: 172px; color: var(--ember-orange);
    font-weight: 700; font-size: 24px; letter-spacing: .5px;
  }
  .contact-list { position: absolute; left: 46px; top: 216px; list-style: none; }
  .contact-list li {
    display: flex; align-items: center; height: 29px;
    color: var(--text-white); font-size: 17px;
  }
  .contact-icon { width: 16px; height: 16px; margin-right: 10px; flex: none; }
  .catering {
    position: absolute; left: 44px; top: 366px; color: var(--ember-orange);
    font-family: "Courgette", cursive; font-size: 23px;
  }

  /* Back */
  .fire-panel { position: absolute; top: 0; width: 205px; height: 429px;
    background: radial-gradient(ellipse at 55% 55%, var(--fire-bright) 0%, var(--fire-mid) 40%, var(--fire-deep) 80%, #2a0a02 100%); }
  .fire-panel--left { left: 0; }
  .fire-panel--right { right: 0; width: 201px;
    background: radial-gradient(ellipse at 45% 40%, var(--fire-bright) 0%, var(--fire-mid) 42%, var(--fire-deep) 80%, #2a0a02 100%); }
  .brand-block { position: absolute; left: 205px; width: 327px; top: 0; height: 429px; text-align: center; }
  .brand-dot { position: absolute; left: 50%; top: 96px; width: 110px; height: 110px; margin-left: -55px;
    border-radius: 50%; background: var(--flame-red); }
  .card--back .brand-name { left: 0; right: 0; top: 274px; font-size: 27px; letter-spacing: 1px; }
  .slogan {
    position: absolute; left: 0; right: 0; top: 372px; color: var(--text-white);
    font-family: "Crimson Pro", serif; font-weight: 600; font-size: 23px;
  }
  .slogan .sep { color: var(--ember-orange); margin: 0 4px; }
</style>
</head>
<body>

<section class="card card--front">
  <svg class="front-photo" viewBox="0 0 400 429" role="img" aria-label="Photo of a wood fired pizza on a peel in the oven, framed by flame shapes">
    <defs>
      <radialGradient id="pizzaGlow" cx="0.45" cy="0.65" r="0.7">
        <stop offset="0" stop-color="var(--cheese)"/>
        <stop offset="0.45" stop-color="var(--crust)"/>
        <stop offset="0.8" stop-color="var(--fire-mid)"/>
        <stop offset="1" stop-color="var(--fire-deep)"/>
      </radialGradient>
    </defs>
    <path d="M400 0 L400 429 L14 429 C0 360 20 270 90 230 C170 185 230 140 250 60 C258 30 255 12 250 0 Z" fill="url(#pizzaGlow)"/>
  </svg>

  <div class="brand-name">QUILLON MAISON</div>

  <h1 class="holder-name">DANA PORRICK</h1>
  <ul class="contact-list">
    <li>
      <svg class="contact-icon" viewBox="0 0 16 16"><path d="M3.5 1.5l2.5 0.5 1 3-1.6 1.2c.8 1.7 2 2.9 3.6 3.6L10.2 8.2l3 1 .5 2.5-1.7 2C6.5 13.5 2.5 9.5 1.8 3.3z" fill="none" stroke="var(--ember-orange)" stroke-width="1.4" stroke-linejoin="round"/></svg>
      570 555 0183
    </li>
    <li>
      <svg class="contact-icon" viewBox="0 0 16 16" fill="none" stroke="var(--ember-orange)" stroke-width="1.3"><circle cx="8" cy="8" r="6.5"/><ellipse cx="8" cy="8" rx="2.8" ry="6.5"/><path d="M1.5 8h13M2.5 4.8h11M2.5 11.2h11"/></svg>
      www.getquillon.example
    </li>
    <li>
      <svg class="contact-icon" viewBox="0 0 16 16"><circle cx="8" cy="8" r="5" fill="var(--ember-orange)"/></svg>
      @getquillonpizza
    </li>
    <li>
      <svg class="contact-icon" viewBox="0 0 16 16"><circle cx="8" cy="8" r="5" fill="var(--ember-orange)"/></svg>
      getquillonpizza
    </li>
  </ul>
  <p class="catering">Catering for all events</p>
</section>

<section class="card card--back">
  <div class="fire-panel fire-panel--left" role="img" aria-label="Photo of burning logs in a wood fire"></div>
  <div class="brand-block">
    <div class="brand-dot"></div>
    <div class="brand-name">QUILLON MAISON</div>
    <p class="slogan">Fast<span class="sep">•</span>Fresh<span class="sep">•</span>Handcrafted</p>
  </div>
  <div class="fire-panel fire-panel--right" role="img" aria-label="Photo of glowing embers and flames in a wood fire"></div>
</section>

</body>
</html>
```